Velvet Lantern Takeaway

we are emergent restaurant, serving high end of vietnamese cuisine.

Takeaway flyer's purpose must catch people attention by visual and clear dishes's description.

Please use attached logo.
And some other design for inspiration.
Updates

FLYER SIZE: DL FOLDED A4- DOUBLED SIZE. I WILL PRINT IT IN FULL COLOR AND 150GSM STOCK PAPER GLOSSTHANKS ALLHOPE I WILL GET A GREAT ONE FROM YOUKAIREN Added Tuesday, February 17, 2015

Please use images of "Vietnamese Beef Noodle PHO" if you intent to use images in the flyer Added Wednesday, February 18, 2015

Industry/Entity Type

Restaurant

Requirements
Must have
• Restaurant logo
Nice to have
• Font is very important.

```html
<!DOCTYPE html>
<html lang="en">
<head>
<meta charset="utf-8">
<title>Velvet Lantern Takeaway – Menu</title>
<link href="https://fonts.googleapis.com/css2?family=Courier+Prime:wght@400;700&family=Fira+Sans:wght@500&display=swap" rel="stylesheet">
<style>
  :root {
    --paper: #cfe7e6;
    --paper-light: #dcefee;
    --teal: #1c8c93;
    --ink: #111416;
    --accent: #f05a1c;
  }
  * { margin: 0; padding: 0; box-sizing: border-box; }
  html, body { width: 1200px; height: 848px; overflow: hidden; }
  body {
    background: radial-gradient(ellipse at 45% 40%, var(--paper-light), var(--paper) 70%);
    font-family: "Courier Prime", "Courier New", monospace;
    color: var(--ink);
    position: relative;
  }
  .menu-section { position: absolute; }
  .col-1 { left: 17px; width: 368px; }
  .col-2 { left: 412px; width: 371px; }
  .col-3 { left: 812px; width: 376px; }

  .section-title {
    display: flex; align-items: center; gap: 8px;
    font-family: "Fira Sans", sans-serif; font-weight: 500;
    font-size: 21px; color: var(--teal); height: 26px;
    margin-bottom: 8px;
  }
  .section-title::before, .section-title::after {
    content: ""; flex: 1; height: 2px; background: var(--teal);
  }
  .col-1 .section-title { padding: 0 40px; }

  .item { margin-bottom: 4px; }
  .row {
    display: flex; align-items: baseline;
    font-weight: 700; font-size: 13px; line-height: 19px;
    white-space: nowrap;
  }
  .leader { flex: 1; overflow: hidden; margin: 0 3px; }
  .leader::before {
    content: "..................................................................................";
  }
  .desc {
    color: var(--accent); font-weight: 700;
    font-size: 10.5px; line-height: 13px;
  }
  .note { font-weight: 700; font-size: 13px; line-height: 19px; }
  .options { padding-left: 12px; margin-bottom: 10px; }
  .sizes {
    color: var(--accent); font-weight: 700; font-size: 13px;
    line-height: 19px; white-space: pre;
  }
</style>
</head>
<body>

<!-- Column one -->
<section class="menu-section col-1" style="top:22px">
  <h2 class="section-title">Entrée</h2>
  <div class="item"><div class="row">Butter Fried Corn (GF)<span class="leader"></span>6.50</div><p class="desc">Fried sweet corn &amp; dried prawn<br>in spring onion butter sauce</p></div>
  <div class="item"><div class="row">Summer Rolls (GF)(2Rolls)<span class="leader"></span>7.50</div><p class="desc">Rice paper rolled with tiger prawns,<br>pork, salads &amp; herbs</p></div>
  <div class="item"><div class="row">Home made Spring Rolls (4pcs)<span class="leader"></span>7.50</div><p class="desc">Pastry wrapped with chicken mince, taro,<br>mushrooms &amp; glass noodles</p></div>
  <div class="item"><div class="row">Prawn Pop (4pcs)<span class="leader"></span>8.50</div><p class="desc">Fried marinated prawn paste on sugar cane sticks</p></div>
  <div class="item"><div class="row">Sugar Cane Beef (4pcs)<span class="leader"></span>7.50</div><p class="desc">Fried lemongrass beef mince on sugar cane sticks</p></div>
  <div class="item"><div class="row">Traditional Vietnamese Fish Cakes<span class="leader"></span>8.50</div><p class="desc">Fried mackerel fish cakes with sweet chilli sauce</p></div>
  <div class="item"><div class="row">Salt &amp; Pepper Squid<span class="leader"></span>12.50</div><p class="desc">Lightly battered pepper salted squid<br>with lemon pepper dipping sauce</p></div>
</section>

<section class="menu-section col-1" style="top:360px">
  <h2 class="section-title">Refreshing Salads</h2>
  <div class="item"><div class="row">Warmed Beef Papaya Salad (GF)<span class="leader"></span>16.90</div><p class="desc">Marinated Beef mixed with green papaya,<br>onion, pickles &amp; herbs</p></div>
  <div class="item"><div class="row">Prawn Papaya Salad (GF)<span class="leader"></span>16.90</div><p class="desc">Prawn salad with lotus pickles, herbs &amp; carrot</p></div>
  <div class="item"><div class="row">Green Apple Salad (GF)<span class="leader"></span>16.90</div><p class="desc">Char-grilled beef slices with green apple salad</p></div>
  <div class="item"><div class="row">Squid Salad (GF)<span class="leader"></span>16.90</div><p class="desc">Steamed squid with herbs, pickles &amp; cucumber</p></div>
  <div class="item"><div class="row">Chicken Salad (GF)<span class="leader"></span>16.90</div><p class="desc">Steamed chicken with plain cabbages,<br>onions, pickles &amp; herbs</p></div>
</section>

<section class="menu-section col-1" style="top:602px">
  <h2 class="section-title">WE LOVE PHO</h2>
  <div class="item"><div class="note">Flat Rice Noodles Soup with Beef</div><div class="sizes">Small ...... 9.00     Regular ...... 14.50</div></div>
  <div class="item"><div class="note">Flat Rice Noodles Soup with Chicken</div><div class="sizes">Small ...... 9.50     Regular ...... 13.50</div></div>
  <div class="item"><div class="note">Flat Rice Noodles Soup<br>with Tofu &amp; Vegetables</div><div class="sizes">Small ...... 9.50     Regular ...... 13.50</div></div>
</section>

<!-- Column two -->
<section class="menu-section col-2" style="top:22px">
  <h2 class="section-title">Vermicelli Noodles Salad</h2>
  <div class="item"><div class="note">Stir-Fry Lemongrass Beef</div><div class="row">with Noodles<span class="leader"></span>13.90</div></div>
  <div class="item"><div class="row">Sugar Cane Beef with Noodles<span class="leader"></span>13.90</div></div>
  <div class="item"><div class="note">Sugar Cane Prawn Cake</div><div class="row">with Noodles<span class="leader"></span>13.90</div></div>
  <div class="item"><div class="row">Chicken Spring Roll with Noodles<span class="leader"></span>13.90</div></div>
  <div class="item"><div class="note">Char-grilled Pork Skewer</div><div class="row">with Noodles<span class="leader"></span>13.90</div></div>
</section>

<section class="menu-section col-2" style="top:223px">
  <h2 class="section-title">Stir-fry Noodles</h2>
  <p class="note">Your choice of:<br>Lemongrass Beef, Chicken, Seafood, Tofu</p>
  <div style="height:13px"></div>
  <div class="row">Stir-fry Egg Noodles<span class="leader"></span>13.90</div>
  <div class="row">Stir-fry Flat Rice Noodles<span class="leader"></span>13.90</div>
  <div class="row">Stir-fry Rice Vermicelli Noodles<span class="leader"></span>13.90</div>
</section>

<section class="menu-section col-2" style="top:374px">
  <h2 class="section-title">Rice Is Nice</h2>
  <div class="item"><div class="row">Coconut Rice - DINNER ONLY<span class="leader"></span>8.90</div><p class="desc">Tasty Steam Rice in Whole Young Coconut.<br>Portion for 2 people</p></div>
  <div class="item"><div class="row">Seafood Fried Rice<span class="leader"></span>15.90</div><p class="desc">Fried rice with prawns &amp; squids,<br>carrots, green beans &amp; corns</p></div>
  <div class="item"><div class="row">Fried Rice<span class="leader"></span>12.90</div><p class="desc">Fried rice with egg, green beans, carrot &amp; corns</p></div>
  <div class="item"><div class="row">Steamed Rice<span class="leader"></span>3.00</div></div>
</section>

<section class="menu-section col-2" style="top:573px">
  <h2 class="section-title">Hot Soup - DINNER</h2>
  <div class="item"><div class="row">Scallop Soup<span class="leader"></span>8.50</div><p class="desc">Thick soup with scallops, egg, corns,<br>carrot, shallots &amp; pepper</p></div>
  <div class="item"><div class="row">Crabmeat &amp; Asparagus Soup<span class="leader"></span>8.50</div><p class="desc">Delicious crabmeat soup with asparagus,<br>egg, carrot shallots &amp; pepper</p></div>
  <div class="item"><div class="row">Vietnamese Signature Hot Sour Soup<span class="leader"></span>8.50</div><p class="desc">Barramundi in sweet and sour soup<br>with bean sprouts, pineapple, tomato &amp; herbs</p></div>
  <div class="item"><div class="row">Chicken Corns Soup<span class="leader"></span>8.50</div><p class="desc">Thick Soup with eggs, carrots, corns,<br>shallot &amp; pepper</p></div>
</section>

<!-- Column three -->
<section class="menu-section col-3" style="top:22px">
  <h2 class="section-title">We mean Green</h2>
  <div class="item"><div class="row">Green Wok Tossed<span class="leader"></span>12.90</div><p class="desc">Asian mixed vegetables with carrot,<br>capsicum &amp; broccoli</p></div>
  <div class="item"><div class="row">Baby Bok Choy with Mushroom<span class="leader"></span>12.90</div>
    <p class="note">Your Choice:</p>
    <p class="desc options">Steam with Soy sauce<br>Steam with Garlic sauce<br>Stir-fry with Soy Sauce<br>Stir-fry with Garlic Sauce</p></div>
  <div class="item"><div class="note">Steam Chinese Broccoli</div><div class="row">with oyster sauce<span class="leader"></span>12.90</div></div>
  <div class="item"><div class="note">Water Spinach tossed with garlic sauce</div><div class="row">(Seasonal)<span class="leader"></span>12.90</div></div>
</section>

<section class="menu-section col-3" style="top:291px">
  <h2 class="section-title">Vegetarian Time</h2>
  <div class="item"><div class="row">Spring Rolls<span class="leader"></span>6.50</div><p class="desc">Fried Pastry wrapped with crushed tofu, taro,<br>mushroom &amp; glass noodles</p></div>
  <div class="item"><div class="row">Winter Rolls<span class="leader"></span>6.50</div><p class="desc">Fried Marinated Tofu Rolls with lettuces,<br>vermicelli &amp; herbs</p></div>
  <div class="item"><div class="row">Salt and Pepper Tofu<span class="leader"></span>11.50</div><p class="desc">Light &amp; crumby pepper salted tofu<br>with onion and shallots</p></div>
  <div class="item"><div class="row">Refreshing Beancurd Salad<span class="leader"></span>13.50</div><p class="desc">Fried bean curd with green salad,<br>cucumber, pickles &amp; herbs</p></div>
  <div class="item"><div class="row">Stir-fry Mushroom and Vegetables<span class="leader"></span>13.50</div><p class="desc">Combination mushroom &amp; mixed Asian green vegetables</p></div>
  <div class="item"><div class="row">Pineapple and Beancurd Wok Tossed<span class="leader"></span>13.50</div><p class="desc">Stir-fry combination bean curd,<br>pineapple &amp; mushrooms</p></div>
  <div class="item"><div class="row">Claypot Tofu and Mushroom<span class="leader"></span>13.50</div><p class="desc">Marinated Tofu andmixed mushroom<br>in soya sauce &amp; coconut juice</p></div>
  <div class="item"><div class="row">Chilli Lemongrass Bean Curd (HOT)<span class="leader"></span>13.50</div><p class="desc">Tofu crusted in lemongrass, capsicum,<br>onions &amp; chilli</p></div>
  <div class="item"><div class="row">Vermicelli Noodles Salad<span class="leader"></span>13.50</div><p class="desc">Marinated fried tofu with vermicelli noodle,<br>salad &amp; herbs</p></div>
  <div class="item"><div class="row">Vegetarian Fried Rice<span class="leader"></span>13.50</div><p class="desc">Fried Rice with Tofu, green beans, corn &amp; carrot</p></div>
  <div class="item"><div class="row">Fried Noodles<span class="leader"></span>13.50</div><p class="desc">Marinated fried tofu Stir fry with noodle,<br>mushroom &amp; bean sprouts</p></div>
</section>

</body>
</html>
```